Architectural Design Build company needs a direct mail flyer

We are a fully service Design Build company who specialize in luxury custom and pre-designed new homes and major home renovations. Our team consists of seasoned architectural, interior design and general contracting professionals all under one roof. We offer clients a transparent, streamlined process to maximize their investment and completion on a timely basis. Leveraging photography and a few before and after and also our Best Builder Awards.

Target Market(s)

Homeowners and buyers between 40-60 years old and financial investment of $300k or more for renovations and $1,000,000 or more for new construction.

Industry/Entity Type

homebuilding and renovations

Colors

Designer to choose colors to be used in the design.

Requirements
Must have
• The construction segments we are focusing this mailer on are transformative renovations and professionally designed custom new homes. . Should have the Pelbrook Before kitchen and after as well as the exterior before and after. and new construction elevation photos.
Nice to have
• WOuld like to see two befores and afters highlighted, mention that are architect and designer are part of the team from start to finish,

```html
<!DOCTYPE html>
<html lang="en">
<head>
<meta charset="utf-8">
<title>VORNE Direct Mail Flyer</title>
<link href="https://fonts.googleapis.com/css2?family=Montserrat:wght@400;500;600;700;800&display=swap" rel="stylesheet">
<style>
:root{
  --page:#e4e4e2;
  --card:#ffffff;
  --ink:#1f2220;
  --dark:#222523;
  --accent:#d2d62c;
  --panel:#efeae2;
  --muted:#5b5e5b;
  --label:#3a3d3b;
}
*{box-sizing:border-box;margin:0;padding:0}
html,body{width:893px;height:1200px;overflow:hidden}
body{background:var(--page);font-family:'Montserrat',sans-serif;color:var(--ink);position:relative}
.side-label{position:absolute;left:80px;font-weight:700;font-size:15px;letter-spacing:1px;color:var(--label)}
.card{position:absolute;left:80px;width:798px;height:490px;background:var(--card);overflow:hidden;box-shadow:0 2px 6px rgba(0,0,0,.15)}
.card--front{top:60px}
.card--back{top:660px}
.brand{font-weight:800;font-size:22px;letter-spacing:1px;display:flex;align-items:center;gap:7px;color:var(--ink)}
.brand-square{width:12px;height:12px;background:var(--accent)}
.front-header{position:absolute;left:0;top:0;width:100%;height:42px;padding:0 22px;display:flex;align-items:center}
.headline{position:absolute;left:22px;top:54px;width:500px;font-weight:800;font-size:22px;line-height:1.12;text-transform:uppercase}
.subline{position:absolute;left:22px;top:108px;font-size:11px;font-weight:500;color:var(--muted)}
.photo{position:absolute}
.hero{left:0;top:130px;width:525px;height:300px;background:linear-gradient(180deg,#b9cfe0 0%,#d6dde0 38%,#e7e5df 60%,#6f7d55 85%,#556640 100%)}
.showcase{position:absolute;left:525px;top:42px;width:273px;height:388px;background:var(--panel);padding:14px 14px}
.showcase-title{font-weight:800;font-size:13px;text-transform:uppercase;margin-bottom:8px}
.pair{display:flex;gap:6px;margin-bottom:26px}
.pair-item{flex:1;background:#fff}
.pair-photo{height:96px}
.pair-tag{font-size:8px;font-weight:700;text-align:center;padding:4px 0;text-transform:uppercase}
.kitchen-before{background:linear-gradient(160deg,#6b4a33,#3b2a1e)}
.kitchen-after{background:linear-gradient(160deg,#f1efe9,#b9b2a5)}
.exterior-before{background:linear-gradient(180deg,#c7d3dc,#8a8676 70%,#6b6a56)}
.exterior-after{background:linear-gradient(180deg,#b7cbdb,#e5e3dc 55%,#5e7045)}
.footer-bar{position:absolute;left:0;bottom:0;width:100%;height:60px;background:var(--dark);display:flex;align-items:center;color:#fff}
.footer-brand{height:100%;width:100px;background:var(--accent);display:flex;align-items:center;justify-content:center;font-weight:800;font-size:18px;letter-spacing:1px;color:var(--ink)}
.footer-text{padding-left:18px;font-size:10px;font-weight:500;display:flex;gap:14px;align-items:center}
.footer-text strong{font-weight:700}
.who{position:absolute;left:28px;top:26px;width:480px}
.who h2{font-weight:800;font-size:28px;text-transform:uppercase;margin-bottom:6px}
.who .tagline{font-weight:700;font-size:11px;text-transform:uppercase;color:#8d8f1c;margin-bottom:8px}
.who p{font-size:10.5px;line-height:1.5;color:var(--muted);margin-bottom:14px}
.who h3{font-weight:800;font-size:12px;text-transform:uppercase;margin-bottom:6px}
.reasons{list-style:none}
.reasons li{display:flex;align-items:center;gap:7px;font-size:10.5px;font-weight:500;margin-bottom:5px}
.reasons svg{flex:none}
.projects{position:absolute;left:548px;top:22px;width:228px}
.project{margin-bottom:8px}
.project-photo{height:68px}
.project-title{font-weight:800;font-size:10px;text-transform:uppercase;margin-top:4px}
.project-note{font-size:8.5px;color:var(--muted)}
.new-home{background:linear-gradient(180deg,#c4d4e0,#ecebe6 55%,#6e7d57)}
</style>
</head>
<body>
<div class="side-label" style="top:34px">FRONT</div>
<section class="card card--front">
  <header class="front-header"><div class="brand"><span class="brand-square"></span>VORNE</div></header>
  <h1 class="headline">Transform your home. Design &amp; build with award-winning experts.</h1>
  <div class="subline">Luxury Renovations &amp; Custom Homes by One Team</div>
  <div class="photo hero" role="img" aria-label="Custom new home exterior with white facade, front porch and lawn"></div>
  <aside class="showcase">
    <div class="showcase-title">Pelbrook Kitchen</div>
    <div class="pair">
      <div class="pair-item"><div class="pair-photo kitchen-before" role="img" aria-label="Kitchen before renovation with dark wood cabinets"></div><div class="pair-tag">Before</div></div>
      <div class="pair-item"><div class="pair-photo kitchen-after" role="img" aria-label="Kitchen after renovation with bright modern finishes"></div><div class="pair-tag">After</div></div>
    </div>
    <div class="showcase-title">Exterior</div>
    <div class="pair">
      <div class="pair-item"><div class="pair-photo exterior-before" role="img" aria-label="Home exterior before renovation"></div><div class="pair-tag">Before</div></div>
      <div class="pair-item"><div class="pair-photo exterior-after" role="img" aria-label="Home exterior after renovation"></div><div class="pair-tag">After</div></div>
    </div>
  </aside>
  <footer class="footer-bar">
    <div class="footer-brand">VORNE</div>
    <div class="footer-text"><strong>Call Now to Schedule a Free Consultation</strong><span>vornebuild.com</span><span>1 (555) 014-2290</span></div>
  </footer>
</section>

<div class="side-label" style="top:634px">BACK</div>
<section class="card card--back">
  <div class="who">
    <h2>Who we are</h2>
    <div class="tagline">One team. One vision. From concept to completion.</div>
    <p>We are a full-service design build company specializing in luxury custom homes and transformative renovations. Our team of architects, designers, and construction professionals work together under one roof to deliver outstanding results — on time and on budget. From your first sketch to the final nail, we ensure your project is as seamless and transparent as it is beautiful.</p>
    <h3>Why choose us</h3>
    <ul class="reasons">
      <li><svg width="12" height="12" viewBox="0 0 12 12"><rect width="12" height="12" fill="#d2d62c"/><path d="M3 6.2l2 2 4-4.4" stroke="#1f2220" stroke-width="1.6" fill="none"/></svg>Architect &amp; Designer Involved from Day One</li>
      <li><svg width="12" height="12" viewBox="0 0 12 12"><rect width="12" height="12" fill="#d2d62c"/><path d="M3 6.2l2 2 4-4.4" stroke="#1f2220" stroke-width="1.6" fill="none"/></svg>In-House Collaboration = Time &amp; Cost Savings</li>
      <li><svg width="12" height="12" viewBox="0 0 12 12"><rect width="12" height="12" fill="#d2d62c"/><path d="M3 6.2l2 2 4-4.4" stroke="#1f2220" stroke-width="1.6" fill="none"/></svg>Award-Winning Luxury Designs</li>
      <li><svg width="12" height="12" viewBox="0 0 12 12"><rect width="12" height="12" fill="#d2d62c"/><path d="M3 6.2l2 2 4-4.4" stroke="#1f2220" stroke-width="1.6" fill="none"/></svg>Clear Timelines &amp; Fixed Budgets</li>
      <li><svg width="12" height="12" viewBox="0 0 12 12"><rect width="12" height="12" fill="#d2d62c"/><path d="M3 6.2l2 2 4-4.4" stroke="#1f2220" stroke-width="1.6" fill="none"/></svg>Premium Materials &amp; Finishes</li>
    </ul>
  </div>
  <div class="projects">
    <div class="project"><div class="project-photo kitchen-after" role="img" aria-label="Remodeled Pelbrook kitchen"></div><div class="project-title">Pelbrook Kitchen Remodel</div><div class="project-note">From dated to designer</div></div>
    <div class="project"><div class="project-photo exterior-after" role="img" aria-label="Renovated home exterior"></div><div class="project-title">Exterior Renovation</div><div class="project-note">Dramatic curb appeal boost</div></div>
    <div class="project"><div class="project-photo new-home" role="img" aria-label="Custom new home elevation"></div><div class="project-title">Custom New Home</div><div class="project-note">Elegant, functional, timeless</div></div>
  </div>
  <footer class="footer-bar">
    <div class="footer-brand">VORNE</div>
    <div class="footer-text"><strong>Call Now to Schedule a Free Consultation</strong><span>1 (555) 014-2290</span></div>
  </footer>
</section>
</body>
</html>
```